This is book 2 to Mirage Harbor. I'm looking for something that feels similar, with the same cymatic image used on Antarctica on the first book cover (see the cover image attached; the original designer said this was the image used: https://www.filevaultexample.net/share/8k2m4p7q9r1t/cymatic-image.png). Differences: the cover should be all black (no Antarctica, no globe, nothing but the image), the cymatic image kind of a pale grayish white (subtle, not calling too much attention to itself. Think the subtle dragon on "The Boy beneath the Copper Lantern"--like that sort of). Same font as before, but red this time (with the color progression like in the first one, only red instead of blue), with the title (Mirage Assault), author name (M.J. Holt), and subtitle (Dawn of the Velorathi, Book 2)

Target Market(s)

adult action/adventure and thriller readers

Industry/Entity Type

media and literature

Colors
EB3D1F
EC4F4E
F09395
F8D3D4
FCEDEE

Requirements
Must have
• look like part of the series before
Should not have
• not too busy

```html
<!DOCTYPE html>
<html lang="en">
<head>
<meta charset="utf-8">
<title>Mirage Assault — M.J. Holt</title>
<link rel="stylesheet" href="https://fonts.googleapis.com/css2?family=Antonio:wght@500&family=Cinzel:wght@500;600&display=swap">
<style>
  :root {
    --backdrop: #dcdcdc;
    --cover-black: #0b0c13;
    --title-dark: #7d1719;
    --title-bright: #ea1c22;
    --subtitle-red: #e8262a;
    --glow-red: #ff3a3a;
    --pattern-pale: #cfd0d3;
    --pattern-mid: #6a6b70;
    --author-white: #ffffff;
  }
  * { margin: 0; padding: 0; box-sizing: border-box; }
  html, body {
    width: 1200px;
    height: 1200px;
    overflow: hidden;
    background: var(--backdrop);
  }
  .book-cover {
    position: absolute;
    left: 219px;
    top: 29px;
    width: 761px;
    height: 1142px;
    background: var(--cover-black);
    overflow: hidden;
  }
  .top-glow {
    position: absolute;
    left: 0;
    top: 0;
    width: 100%;
    height: 160px;
    background: radial-gradient(ellipse 55% 100% at 50% 0%, rgba(170, 40, 45, 0.75), rgba(90, 20, 25, 0.25) 55%, transparent 80%);
  }
  .title {
    position: absolute;
    left: 0;
    width: 100%;
    text-align: center;
    font-family: "Antonio", "Oswald", sans-serif;
    font-weight: 500;
    text-transform: uppercase;
    line-height: 1;
    font-size: 195px;
    letter-spacing: 2px;
    background: linear-gradient(to bottom, var(--title-dark) 18%, var(--title-bright) 62%, var(--title-bright) 80%, var(--title-dark) 100%);
    -webkit-background-clip: text;
    background-clip: text;
    color: transparent;
  }
  .title-line-one { top: 48px; }
  .title-line-two { top: 240px; }
  .series-band {
    position: absolute;
    left: 0;
    top: 425px;
    width: 100%;
    height: 104px;
    background: linear-gradient(to bottom, transparent, rgba(120, 10, 12, 0.35) 30%, rgba(120, 10, 12, 0.35) 70%, transparent);
  }
  .band-line {
    position: absolute;
    left: 3%;
    width: 94%;
    height: 3px;
    background: linear-gradient(to right, transparent, var(--glow-red) 20%, #ffb0b0 50%, var(--glow-red) 80%, transparent);
    box-shadow: 0 0 10px 3px rgba(255, 40, 40, 0.55);
  }
  .band-line-top { top: 24px; }
  .band-line-bottom { top: 80px; }
  .series-name {
    position: absolute;
    left: 0;
    top: 37px;
    width: 100%;
    text-align: center;
    font-family: "Cinzel", "Trajan Pro", serif;
    font-weight: 600;
    font-size: 31px;
    letter-spacing: 1px;
    line-height: 1;
    color: var(--subtitle-red);
  }
  .cymatic-art {
    position: absolute;
    left: 0;
    top: 545px;
    width: 100%;
    height: 597px;
    background: radial-gradient(ellipse 70% 85% at 50% 100%, rgba(0,0,0,0.9) 0%, rgba(0,0,0,0.6) 22%, transparent 40%),
                radial-gradient(ellipse 80% 95% at 50% 100%, var(--pattern-pale) 0%, var(--pattern-mid) 55%, transparent 90%);
    opacity: 0.7;
  }
  .author {
    position: absolute;
    left: 0;
    top: 992px;
    width: 100%;
    text-align: center;
    font-family: "Cinzel", "Trajan Pro", serif;
    font-weight: 500;
    font-size: 48px;
    letter-spacing: 1px;
    line-height: 1.2;
    color: var(--author-white);
  }
</style>
</head>
<body>
  <main class="book-cover">
    <div class="top-glow"></div>
    <h1>
      <span class="title title-line-one">Mirage</span>
      <span class="title title-line-two">Assault</span>
    </h1>
    <div class="series-band">
      <span class="band-line band-line-top"></span>
      <p class="series-name">DAWN OF THE VELORATHI, BOOK 2</p>
      <span class="band-line band-line-bottom"></span>
    </div>
    <div class="cymatic-art" role="img" aria-label="Pale grayish-white cymatic pattern of radiating petal-like sound-wave loops fanning out from the bottom center"></div>
    <p class="author">M.J. HOLT</p>
  </main>
</body>
</html>
```